"sweetpalazzo!" hand crafted, premium gelato needs a delicious design!

SweetPalazzo!
Hand Crafted, Premium, Delicious (tag line to be included)

We are artisan gelato craftsmen, passionate about the art of making gelato. Our philosophy to crafting our premium gelato is pure and simple.
Always use quality fresh ingredients
Keep learning, always improving and honing our gelato crafting skills
We believe that this simple philosophy is the key to our Delicious, Premium and Authentic gelato that is SweetPalzzo!

Where possible, we source our key ingredients from local producers who in their own right are proud and passionate about their produce.

The logo should be clean and communicate a premium, artisan, hand crafted product.

I will require a front label which describes the flavor of the gelato and a rear ingredients/nutritional facts label.

The rear label needs to be easily modifiable according to the flavor and ingredients used, as we add to our flavor list.

There should also be a space to insert a nutrition label - I've uploaded an example of a nutrition label

As an example for rear label

___________________________________________________________________________
Our artisan Gelato is proudly hand crafted in small batches with love, passion and with local Australian produce whenever possible. We use Fresh Milk and Pure Cream sourced from local producers who are equally passionate about their produce.

We only use All Natural ingredients. Free from any artificial colours, flavours, and preservatives.

Ingredients
Fresh Milk, Pure Cream, Skim Milk Powder, Sugar, Dextrose, Japanese Matcha, Arrowroot Flour. Guar Gum

Contains Milk, Wheat

Although we do not use nuts, some of the ingredients we use may have been processed on equipment that may have processed nuts.

Best Stored Frozen at minus 18°C

We would love to hear from you!
www.sweetpalazzo.com.au
gelato@sweetpalazzo.com.au
(place facebook logo here)

Example of a label I like:

http://www.wrapgallery.example/tondo-artisan-gelato.html/

I would like to showcase the end product as much as possible so the label should be transparent and enhance the flavor of the gelato. A small graphic complimenting the key ingredient the flavor would be enhancing the product.

Some of the examples of the flavors we have are
Japanese Matcha * this will be the main flavour
Bellwether Ridge Chocolate Bar
Tumbleweed Creek Salted Caramel
Vanilla Bean

Please note that there is future paid opportunity to make modifications to the front label and ingredients label as we keep adding flavors so I am looking for a designer that I can have a long term partnership with. Thanks! Added Wednesday, October 12, 2016

Target Market(s)

Retail space looking for a premium alternative to the high end ice cream. People who appreciate artisan products

Logo Text

SweetPalazzo!- Premium, Hand Crafted, Delicious

Requirements
Must have
• must highlight the key ingredient of each flavor

```html
<!DOCTYPE html>
<html lang="en">
<head>
<meta charset="utf-8">
<title>SweetPalazzo! Front Label</title>
<link rel="stylesheet" href="https://fonts.googleapis.com/css2?family=Satisfy&family=Roboto:wght@400&display=block">
<style>
  :root {
    --parchment-light: #ecd08e;
    --parchment-mid: #e4c27c;
    --parchment-edge: #c99a4f;
    --ink: #231a12;
    --pill: #c3957a;
    --band: #c9977c;
    --haze: #dcbb82;
    --hill-far: #cfa96e;
    --hill-mid: #b48c5b;
    --forest: #8f6b45;
    --forest-deep: #7a5a3a;
    --river: #ead29a;
    --footer-ink: #2b2118;
    --script: "Satisfy", "Segoe Script", "Brush Script MT", "Apple Chancery", cursive;
  }
  html, body {
    margin: 0;
    padding: 0;
    width: 1200px;
    height: 960px;
    overflow: hidden;
    background: #ffffff;
  }
  .label {
    position: relative;
    width: 1200px;
    height: 960px;
    background: radial-gradient(ellipse at 45% 35%, var(--parchment-light) 0%, var(--parchment-mid) 55%, var(--parchment-edge) 100%);
    overflow: hidden;
  }
  .brand {
    position: absolute;
    top: 205px;
    left: 0;
    width: 100%;
    margin: 0;
    text-align: center;
    font-family: var(--script);
    font-weight: 400;
    font-size: 104px;
    line-height: 1.1;
    color: var(--ink);
  }
  .tagline {
    position: absolute;
    top: 352px;
    left: 0;
    width: 100%;
    margin: 0;
    text-align: center;
    font-family: var(--script);
    font-size: 30px;
    line-height: 1.2;
    color: var(--ink);
  }
  .flavour {
    position: absolute;
    top: 500px;
    left: 50%;
    transform: translateX(-50%);
    padding: 6px 30px 8px;
    border-radius: 30px;
    background: var(--pill);
    font-family: var(--script);
    font-size: 33px;
    line-height: 1.2;
    color: var(--ink);
    white-space: nowrap;
  }
  .landscape {
    position: absolute;
    left: 0;
    top: 570px;
    width: 1200px;
    height: 360px;
    background:
      radial-gradient(ellipse 30% 14% at 48% 94%, var(--river) 0%, rgba(234,210,154,0) 100%),
      radial-gradient(ellipse 22% 60% at 15% 100%, var(--forest-deep) 0%, rgba(122,90,58,0) 100%),
      radial-gradient(ellipse 25% 65% at 88% 100%, var(--forest-deep) 0%, rgba(122,90,58,0) 100%),
      radial-gradient(ellipse 28% 38% at 20% 18%, var(--hill-far) 0%, rgba(207,169,110,0) 100%),
      radial-gradient(ellipse 35% 40% at 55% 60%, var(--hill-mid) 0%, rgba(180,140,91,0) 100%),
      linear-gradient(180deg, rgba(220,187,130,0) 0%, var(--haze) 22%, var(--hill-far) 45%, var(--hill-mid) 70%, var(--forest) 100%);
  }
  .contact-band {
    position: absolute;
    left: 0;
    bottom: 0;
    width: 100%;
    height: 30px;
    background: var(--band);
    display: flex;
    justify-content: center;
    align-items: center;
    gap: 22px;
    font-family: "Roboto", sans-serif;
    font-size: 15px;
    color: var(--footer-ink);
  }
  .contact-item {
    display: flex;
    align-items: center;
    gap: 6px;
  }
  .contact-item svg {
    width: 15px;
    height: 15px;
  }
</style>
</head>
<body>
  <div class="label">
    <h1 class="brand">SweetPalazzo!</h1>
    <p class="tagline">Hand Crafted. Premium. Delicious</p>
    <div class="flavour">Tumbleweed Creek Salted Caramel</div>

    <div class="landscape" role="img" aria-label="Illustrated landscape of misty mountains, pine forests and a calm river in warm caramel tones"></div>

    <div class="contact-band">
      <span class="contact-item">
        <svg viewBox="0 0 16 16" aria-hidden="true">
          <circle cx="8" cy="8" r="6.5" fill="none" stroke="currentColor" stroke-width="1.3"/>
          <ellipse cx="8" cy="8" rx="3" ry="6.5" fill="none" stroke="currentColor" stroke-width="1.1"/>
          <line x1="1.5" y1="8" x2="14.5" y2="8" stroke="currentColor" stroke-width="1.1"/>
        </svg>
        www.sweetpalazzo.com.au
      </span>
      <span class="contact-item">
        <svg viewBox="0 0 16 16" aria-hidden="true">
          <rect x="1.5" y="3.5" width="13" height="9" fill="none" stroke="currentColor" stroke-width="1.3"/>
          <polyline points="1.5,3.5 8,9 14.5,3.5" fill="none" stroke="currentColor" stroke-width="1.3"/>
        </svg>
        gelato@sweetpalazzo.com.au
      </span>
      <span class="contact-item">
        <svg viewBox="0 0 16 16" aria-hidden="true">
          <circle cx="8" cy="8" r="5" fill="currentColor"/>
        </svg>
        sweetpalazzo
      </span>
    </div>
  </div>
</body>
</html>
```